Tin Lark Candle Co. 3x3x3 reverse tuck product box

Coconut wax candles in paint cans. Fun, unpretentious. Every label has a different design that reflects the candle scent. Eclectic but simple branding. I want to take a minimalist approach as I need one box design to work for all of my product. Since my candles are so colorful and unique, I like Black and white (like my logo) on Kraft background. No candle names on the box, just my logo and welcome message on the back of the box with pertinent info (see "must haves"). Need to reflect my brand in one box that will work with my many unique labels. Company logo is black & white. I need to fit a particular template for printing. I really like the idea of a kraft background, but it would need to be a vector as my printing company cannot print white ink on kraft boxes. I am very open to non-kraft related art if it looks great! Please see requirement document. I have uploaded some of my product so the general feel of the brand is available. One candle per box. My website is www.tinlarkcandle.example. My website and marketing material is minimalist since my each of my products are very unique and busy. Feel free to read my product descriptions to get a feel for my brand.

Target Market(s)

18-45 year olds

Industry/Entity Type

Candles/gifts

Font styles to use
Other font styles liked:
• NOW

Colors

Designer to choose colors to be used in the design.

Requirements
Must have
• My business logo, cruelty free logo, Paraben-free logo, recyclable , and handmade in Austin, TX
Nice to have
• I've uploaded a pic with back of box text I would like to see. My company tagline is: Coconut Wax Candle Awesomeness.
Should not have
• My candle label art on the box. I have many unique labels, and I will need this box to work for all of them.

```html
<!DOCTYPE html>
<html lang="en">
<head>
<meta charset="utf-8">
<title>Tin Lark Candle Co. — Reverse Tuck Box Dieline</title>
<link rel="stylesheet" href="https://fonts.googleapis.com/css2?family=Jost:wght@400;700;800&family=Montserrat:wght@700;800&display=swap">
<style>
  :root {
    --kraft: #c8a27a;
    --fold: #7fa9b3;
    --ink: #111111;
    --paper: #ffffff;
    --page: #ffffff;
    --slot: #f1ece4;
  }
  html, body {
    margin: 0;
    padding: 0;
    width: 1200px;
    height: 554px;
    overflow: hidden;
    background: var(--page);
  }
  .dieline { display: block; width: 1200px; height: 554px; }
  .kraft { fill: var(--kraft); }
  .fold { stroke: var(--fold); stroke-width: 1.2; fill: none; }
  .spec-label { font-family: "Montserrat", sans-serif; font-weight: 700; font-size: 12px; fill: var(--ink); }
  .spec-label .light { font-weight: 400; }
  .side-title { font-family: "Montserrat", sans-serif; font-weight: 800; font-size: 40px; fill: var(--ink); }
  .headline-small { font-family: "Montserrat", sans-serif; font-weight: 800; font-size: 11px; fill: var(--ink); }
  .welcome-box { fill: var(--paper); stroke: var(--ink); stroke-width: 1.5; }
  .welcome-text { font-family: "Montserrat", sans-serif; font-weight: 800; font-size: 11.4px; fill: var(--ink); }
  .badge { fill: var(--paper); stroke: var(--ink); stroke-width: 1.5; }
  .badge-text { font-family: "Montserrat", sans-serif; font-weight: 800; fill: var(--ink); }
  .bubble { fill: var(--paper); stroke: var(--ink); stroke-width: 1.5; }
  .bubble-text { font-family: "Montserrat", sans-serif; font-weight: 700; font-size: 6px; fill: var(--ink); }
  .art-slot { fill: var(--slot); stroke: var(--ink); stroke-width: 1.2; }
  .logo-frame { fill: var(--paper); stroke: var(--ink); stroke-width: 1.5; }
  .logo-name { font-family: "Jost", sans-serif; font-weight: 400; fill: var(--ink); }
  .brand-word { font-family: "Jost", sans-serif; font-weight: 700; fill: var(--ink); }
  .brand-word-giant { font-family: "Jost", sans-serif; font-weight: 800; fill: var(--ink); }
  .tagline { font-family: "Montserrat", sans-serif; font-weight: 700; font-size: 6.2px; fill: var(--ink); }
  .net-tab { fill: var(--paper); stroke: var(--ink); stroke-width: 1.2; }
  .side-strip { fill: var(--paper); stroke: var(--ink); stroke-width: 1.5; }
  .rule { stroke: var(--ink); stroke-width: 4; }
</style>
</head>
<body>
<svg class="dieline" viewBox="0 0 2004 940" preserveAspectRatio="xMidYMid meet" xmlns="http://www.w3.org/2000/svg">
  <defs>
    <g id="box-net">
      <polygon class="kraft" points="10,320 53,313 53,528 10,522"/>
      <path class="kraft" d="M53,313 V95 Q53,42 103,42 H218 Q268,42 268,95 V313 Z"/>
      <polygon class="kraft" points="285,205 455,205 478,295 484,313 269,313 275,295"/>
      <polygon class="kraft" points="730,205 898,205 905,295 914,313 699,313 705,295"/>
      <rect class="kraft" x="53" y="313" width="861" height="215"/>
      <polygon class="kraft" points="269,528 484,528 474,542 468,636 298,636 276,542"/>
      <polygon class="kraft" points="699,528 914,528 906,542 886,636 718,636 709,542"/>
      <path class="kraft" d="M484,528 H699 V750 Q699,800 649,800 H534 Q484,800 484,750 Z"/>
      <path class="fold" d="M53,313 H914 M53,528 H914 M53,313 V528 M269,313 V528 M484,313 V528 M699,313 V528 M70,100 H250 M500,742 H684"/>
    </g>
  </defs>

  <text class="spec-label" x="10" y="10">Card Box <tspan class="light">76×76×76 mm</tspan></text>
  <text class="spec-label" x="1099" y="10">Card Box <tspan class="light">76×76×76 mm</tspan></text>

  <!-- OUTSIDE -->
  <g class="net net-outside">
    <use href="#box-net"/>

    <g class="panel-back">
      <text class="headline-small" x="59" y="345" textLength="84" lengthAdjust="spacingAndGlyphs">HANDMADE IN</text>
      <rect class="art-slot" x="147" y="326" width="17" height="21" role="img" aria-label="Small Texas state outline"/>
      <text class="headline-small" x="168" y="345" textLength="94" lengthAdjust="spacingAndGlyphs">AUSTIN, TX Y'ALL</text>
      <rect class="welcome-box" x="59" y="360" width="203" height="112"/>
      <text class="welcome-text" text-anchor="middle">
        <tspan x="161" y="374">HI, I'M YOUR AWESOME NEW</tspan>
        <tspan x="161" y="388.5">TIN LARK CANDLE. YOU</tspan>
        <tspan x="161" y="403">OBVIOUSLY HAVE EXCELLENT</tspan>
        <tspan x="161" y="417.5">TASTE AND A GREAT SENSE OF</tspan>
        <tspan x="161" y="432">HUMOR. KEEP IT UP. THE</tspan>
        <tspan x="161" y="446.5">WORLD NEEDS MORE PEOPLE</tspan>
        <tspan x="161" y="461">LIKE YOU.</tspan>
      </text>
      <circle class="badge" cx="93" cy="502" r="13" role="img" aria-label="Recyclable badge"/>
      <circle class="badge" cx="150" cy="502" r="15" role="img" aria-label="Cruelty free badge"/>
      <rect class="badge" x="192" y="490" width="14" height="22" role="img" aria-label="Paraben free badge"/>
      <text class="badge-text" font-size="8" x="210" y="499">+PARABEN</text>
      <text class="badge-text" font-size="13" x="218" y="511">FREE</text>
    </g>

    <g class="panel-side">
      <path class="bubble" d="M342,364 Q376,358 413,364 L414,402 Q378,408 352,403 L344,412 L346,403 Q340,400 340,396 Z"/>
      <text class="bubble-text" text-anchor="middle">
        <tspan x="378" y="381">SMELLS SO GOOD</tspan>
        <tspan x="378" y="392">UP IN HERE</tspan>
      </text>
      <rect class="art-slot" x="355" y="415" width="40" height="52" role="img" aria-label="Line drawing of a milk carton"/>
    </g>

    <g class="panel-front">
      <rect class="logo-frame" x="527" y="368" width="128" height="46" rx="5"/>
      <text class="logo-name" font-size="12" x="591" y="395" text-anchor="middle">Tin Lark candle co.</text>
      <text class="brand-word" font-size="30" x="591" y="457" text-anchor="middle">Tin Lark</text>
      <text class="tagline" x="591" y="507" text-anchor="middle">184 GRAMS OF COCONUT WAX CANDLE AWESOMENESS</text>
      <path class="net-tab" d="M560,530 V523 Q560,518 566,518 H618 Q624,518 624,523 V530 Z"/>
      <text class="tagline" x="592" y="526" text-anchor="middle">6.5 OZ</text>
    </g>

    <g class="panel-spine">
      <rect class="side-strip" x="780" y="314" width="52" height="214"/>
      <text class="brand-word" font-size="30" transform="translate(796,421) rotate(90)" text-anchor="middle">Tin Lark</text>
    </g>
  </g>
  <text class="side-title" x="0" y="820">OUTSIDE</text>

  <!-- INSIDE -->
  <g class="net net-inside">
    <use href="#box-net" transform="translate(1089,0)"/>
    <rect class="logo-frame" x="1162" y="392" width="178" height="65" rx="6"/>
    <text class="logo-name" font-size="14" x="1251" y="430" text-anchor="middle">Tin Lark candle co.</text>
    <text class="brand-word-giant" font-size="112" x="1370" y="458" textLength="615" lengthAdjust="spacing">Tin Lark</text>
    <line class="rule" x1="1803" y1="475" x2="1984" y2="475"/>
  </g>
  <text class="side-title" x="1108" y="820">INSIDE</text>
</svg>
</body>
</html>
```